Concierge Clearline / Medical Supply Ordering Business - Sleek, Efficient, Professional, Elite

www.brixtonfaymedical.example - example website.

We are a concierge supply ordering business for medical and dental that provide DSO price savings on supplies while maintaining business autonomy and independence.

We want a very simple website that looks very professional says what we do and gives a very simple method to contact us & sign up as above.

Target Market(s)

Independent Clearline and Medical Practices

Industry/Entity Type

Clearline and Medical - healthcare

Coding

Coded - Design and coding required

Number of Pages Required

3 page

Font styles to use
Sans Serif

Colors
0054AA
0677BA
7BADD7
CADEEF
E8F1F8

Requirements
Must have
• Simple contact page, sleek efficient design, uncomplicated.
Nice to have
• Sign up page vs just a contact page.
Should not have
• Lots of pages, hard to navigate,

```html
<!DOCTYPE html>
<html lang="en">
<head>
<meta charset="utf-8">
<title>Clearline Supply — Supply Ordering Solutions</title>
<link href="https://fonts.googleapis.com/css2?family=Hind:wght@400;500;600;700&family=Montserrat:wght@300;400;500;600&display=swap" rel="stylesheet">
<style>
:root{
  --navy:#0f1f4b;
  --navy-deep:#0a1738;
  --teal:#0ea2d0;
  --ink:#16213a;
  --muted:#6b7385;
  --soft:#eef1f6;
  --white:#ffffff;
  --line:#d9dde5;
}
*{box-sizing:border-box;margin:0;padding:0}
html,body{width:1200px;height:4729px;overflow:hidden}
body{position:relative;background:var(--white);font-family:"Montserrat",sans-serif;color:var(--ink)}
.abs{position:absolute}
.head{font-family:"Hind",sans-serif}
.photo{position:absolute}

/* header */
.topbar{left:385px;top:0;width:815px;height:31px;background:var(--navy);display:flex;align-items:center;font-size:11px;color:#fff;font-weight:600}
.topbar .item{display:flex;align-items:center;gap:7px;height:100%}
.topbar .phone{padding-left:60px;width:208px}
.topbar .appt{background:var(--teal);width:252px;justify-content:center;font-size:10px}
.topbar .addr{padding-left:24px;font-size:10px}
.brand{left:120px;top:28px;display:flex;align-items:center;gap:8px;font-family:"Hind",sans-serif;font-weight:700;font-size:20px;color:var(--navy)}
.brand .mark{width:20px;height:20px;background:var(--teal)}
.nav{top:58px;left:396px;width:360px;height:16px;font-size:11px;font-weight:500;color:var(--ink)}
.nav a{position:absolute;top:0;white-space:nowrap;text-decoration:none;color:inherit}
.btn-outline{left:932px;top:52px;width:118px;height:31px;border:1px solid var(--teal);border-radius:3px;font-size:10px;font-weight:500;display:flex;align-items:center;justify-content:center;color:var(--navy)}

/* hero */
.hero{left:0;top:100px;width:1200px;height:616px;background:linear-gradient(120deg,#3b3f47 0%,#5a5550 40%,#2c2f35 100%)}
.hero::after{content:"";position:absolute;inset:0;background:rgba(10,18,40,.55)}
.welcome{left:517px;top:299px;width:162px;height:35px;background:var(--teal);color:#fff;font-size:12px;font-weight:600;display:flex;align-items:center;justify-content:center;z-index:2}
.hero-title{left:0;top:350px;width:1200px;text-align:center;color:#fff;font-size:58px;line-height:68px;font-weight:600;z-index:2}
.hero-btn{left:515px;top:517px;width:166px;height:44px;border:1px solid #fff;color:#fff;font-size:12px;font-weight:600;display:flex;align-items:center;justify-content:center;z-index:2}

/* about */
.eyebrow{font-size:11px;color:var(--teal);font-weight:500;text-transform:uppercase}
.eyebrow.center{text-align:center;width:1200px;left:0}
.eyebrow span{border-bottom:1px solid var(--teal);padding-bottom:3px}
.h2{font-family:"Hind",sans-serif;font-weight:600;font-size:42px;line-height:52px;color:var(--navy)}
.h2.center{text-align:center;width:1200px;left:0}
.para{font-size:12px;line-height:21px;color:var(--muted)}
.btn-teal{background:var(--teal);color:#fff;font-size:14px;font-weight:600;display:flex;align-items:center;justify-content:center;gap:12px}
.badge-circle{left:295px;top:996px;width:100px;height:100px;border-radius:50%;background:#fff;display:flex;align-items:center;justify-content:center}
.badge-circle div{width:44px;height:44px;background:var(--teal)}

/* services */
.services-bg{left:0;top:1321px;width:1200px;height:652px;background:var(--soft)}
.svc-img{top:1597px;width:325px;height:260px}
.svc-icon{top:1547px;width:100px;height:100px;border-radius:50%;background:var(--navy);border:6px solid var(--soft);display:flex;align-items:center;justify-content:center}
.svc-label{top:1813px;width:271px;height:95px;background:#fff;box-shadow:0 8px 20px rgba(15,31,75,.08);display:flex;align-items:center;justify-content:center;font-family:"Hind",sans-serif;font-size:20px;font-weight:500;color:var(--navy)}

/* cta */
.cta{left:0;top:1973px;width:1200px;height:257px;background:var(--navy)}
.cta-title{left:0;top:2056px;width:1200px;text-align:center;color:#fff;font-family:"Hind",sans-serif;font-size:35px;line-height:39px;font-weight:500}
.cta-title em{font-style:normal;color:var(--teal)}
.contact-bar{left:350px;top:2198px;width:500px;height:55px;background:#fff;box-shadow:0 6px 20px rgba(0,0,0,.1);display:flex;align-items:center;justify-content:space-around;font-size:15px;font-weight:500;color:var(--ink);z-index:3}

/* why */
.why-photo{left:770px;top:2230px;width:430px;height:838px}
.why-card{width:232px;height:261px;background:#fff;box-shadow:0 6px 18px rgba(15,31,75,.08);text-align:center;padding-top:30px}
.why-card .ic{width:82px;height:82px;border-radius:50%;background:#f0f2f5;margin:0 auto 22px;display:flex;align-items:center;justify-content:center}
.why-card h3{font-family:"Hind",sans-serif;font-size:20px;font-weight:500;color:var(--navy);margin-bottom:4px}
.why-card p{font-size:13px;line-height:23px;color:var(--ink);padding:0 20px}
.why-card.active{background:var(--teal)}
.why-card.active h3,.why-card.active p{color:#fff}
.why-card.active .ic{background:#fff}

/* testimonials */
.test-band{left:0;top:3068px;width:1200px;height:360px;background:linear-gradient(180deg,#1a2b5c,#0f1f4b)}
.t-card{top:3309px;width:301px;height:324px;background:#fff;box-shadow:0 6px 20px rgba(15,31,75,.1);padding:42px 38px 0 40px}
.t-card .stars{color:#e8523f;font-size:18px;letter-spacing:4px}
.t-card p{font-size:13px;line-height:25px;color:var(--muted);margin-top:10px}
.t-card hr{border:0;border-top:1px solid #9aa0ab;margin:32px 0 22px}
.t-card .who{display:flex;align-items:center;gap:14px}
.t-card .av{width:56px;height:56px;border-radius:50%;background:linear-gradient(135deg,#c9ccd3,#8a8f99)}
.t-card .nm{font-family:"Hind",sans-serif;font-weight:500;font-size:15px;color:var(--ink)}
.t-card .rl{font-size:13px;color:var(--muted)}
.quote{top:3343px;width:52px;height:52px;border-radius:50%;background:var(--teal);color:#fff;font-family:"Hind",sans-serif;font-size:44px;font-weight:700;display:flex;align-items:center;justify-content:center;line-height:1;padding-top:18px}

/* contact */
.contact-card{position:absolute;left:138px;top:3868px;width:921px;height:457px;background:#fff;border-radius:14px;box-shadow:0 10px 30px rgba(15,31,75,.12);overflow:hidden;z-index:3}
.contact-photo{left:0;top:0;width:458px;height:457px}
.form-brand{left:512px;top:48px;display:flex;align-items:center;gap:8px;font-family:"Hind",sans-serif;font-weight:700;font-size:18px;color:var(--navy)}
.form-brand .mark{width:16px;height:16px;background:var(--teal)}
.form-title{left:512px;top:108px;font-family:"Hind",sans-serif;font-size:29px;color:var(--navy)}
.field{border:1px solid var(--line);font-size:11px;color:var(--muted);padding:10px 8px}
.send{left:512px;top:363px;width:360px;height:37px;background:var(--teal);color:#fff;font-size:12px;font-weight:600;display:flex;align-items:center;justify-content:center;border-radius:2px}

/* footer */
.footer{left:0;top:4180px;width:1200px;height:490px;background:var(--navy-deep)}
.footer-brand{left:0;top:4400px;width:1200px;text-align:center;font-family:"Hind",sans-serif;font-weight:700;font-size:24px;color:#fff}
.footer-brand .mark{display:inline-block;width:18px;height:18px;background:var(--teal);margin-right:10px;vertical-align:-1px}
.fnav{top:4490px;left:0;width:1200px;height:20px;font-size:14px;color:#fff}
.fnav span{position:absolute;top:0;white-space:nowrap}
.fline{left:142px;top:4542px;width:918px;height:1px;background:rgba(255,255,255,.35)}
.finfo{top:4585px;display:flex;align-items:center;gap:14px;color:#fff;font-size:12px;line-height:18px}
.finfo .ring{width:54px;height:54px;border-radius:50%;border:1px solid rgba(255,255,255,.7);display:flex;align-items:center;justify-content:center}
.finfo b{font-weight:500;font-size:14px}
.fdiv{top:4580px;width:1px;height:66px;background:rgba(255,255,255,.35)}
.bottom{left:0;top:4670px;width:1200px;height:59px;background:var(--teal);color:#fff;font-size:12px}
.bottom .copy{position:absolute;left:148px;top:22px}
.social{position:absolute;top:18px;width:24px;height:24px;border:1px solid #fff;border-radius:3px}
</style>
</head>
<body>

<!-- header -->
<div class="abs topbar">
  <div class="item phone">
    <svg width="14" height="14" viewBox="0 0 24 24" fill="none" stroke="#fff" stroke-width="2"><path d="M22 16.9v3a2 2 0 0 1-2.2 2 19.8 19.8 0 0 1-8.6-3.1 19.5 19.5 0 0 1-6-6A19.8 19.8 0 0 1 2.1 4.2 2 2 0 0 1 4.1 2h3a2 2 0 0 1 2 1.7c.1.9.4 1.8.7 2.7a2 2 0 0 1-.5 2.1L8 9.8a16 16 0 0 0 6 6l1.3-1.3a2 2 0 0 1 2.1-.5c.9.3 1.8.6 2.7.7a2 2 0 0 1 1.7 2z"/></svg>
    512 - 555 - 0148
  </div>
  <div class="item appt">
    <svg width="13" height="13" viewBox="0 0 24 24" fill="none" stroke="#fff" stroke-width="2"><rect x="3" y="4" width="18" height="17"/><path d="M3 9h18M8 2v4M16 2v4"/></svg>
    REQUEST AN APPOINTMENT
  </div>
  <div class="item addr">
    <svg width="12" height="13" viewBox="0 0 24 24" fill="none" stroke="#fff" stroke-width="2"><path d="M12 22s7-7 7-12a7 7 0 0 0-14 0c0 5 7 12 7 12z"/><circle cx="12" cy="10" r="2.5"/></svg>
    88 Harbor Lane, Suite 4
  </div>
</div>

<div class="abs brand"><span class="mark"></span>Clearline</div>

<nav class="abs nav">
  <a style="left:0">Home</a>
  <a style="left:76px">About Us</a>
  <a style="left:149px">Services</a>
  <a style="left:224px">Our Team</a>
  <a style="left:312px">Blog</a>
</nav>
<div class="abs btn-outline">CONTACT US</div>

<!-- hero -->
<div class="photo hero" role="img" aria-label="Business team smiling and shaking hands in a meeting"></div>
<div class="abs welcome">WELCOME</div>
<h1 class="abs hero-title head">Supply Ordering Solutions for<br>Medical Success</h1>
<div class="abs hero-btn">ABOUT COMPANY</div>

<!-- about -->
<div class="photo" style="left:88px;top:862px;width:246px;height:364px;background:linear-gradient(160deg,#c9ced6,#8a919c)" role="img" aria-label="Colleagues reviewing work at a laptop"></div>
<div class="photo" style="left:349px;top:817px;width:225px;height:220px;background:linear-gradient(160deg,#9aa4b2,#5f6978)" role="img" aria-label="Team discussing in a modern office"></div>
<div class="photo" style="left:349px;top:1050px;width:225px;height:222px;background:linear-gradient(160deg,#b7bcc5,#6c7382)" role="img" aria-label="Two colleagues working on a tablet"></div>
<div class="abs badge-circle"><div></div></div>

<div class="abs eyebrow" style="left:618px;top:812px"><span>WHO WE ARE</span></div>
<h2 class="abs h2" style="left:618px;top:848px;font-size:42px;line-height:54px">Your Supply Ordering<br>Partner for Success</h2>
<div class="abs head" style="left:618px;top:980px;font-size:21px;font-weight:500;color:var(--ink)">Efficiency, Accuracy, Growth</div>
<p class="abs para" style="left:618px;top:1022px;width:505px">Lorem ipsum dolor sit amet, consectetur adipiscing elit, sed do eiusmod temp or incididunt ut labore et dolore magna aliqua. Ut enim ad minim veniam, quis labois nisi ut aliquip ex ea commodo consequat.</p>
<p class="abs para" style="left:618px;top:1097px;width:505px">Lorem ipsum dolor sit amet, consectetur adipiscing elit, sed do eiusmod temp or incididunt ut labore et dolore magna aliqua.</p>
<div class="abs btn-teal" style="left:618px;top:1182px;width:153px;height:42px">Contact us
  <svg width="18" height="12" viewBox="0 0 18 12" fill="none" stroke="#fff" stroke-width="1.6"><path d="M0 6h16M11 1l5 5-5 5"/></svg>
</div>

<!-- services -->
<div class="abs services-bg"></div>
<div class="abs eyebrow center" style="top:1399px"><span>OUR SERVICES</span></div>
<h2 class="abs h2 center" style="top:1434px">Leading Supply Ordering Services</h2>

<div class="photo svc-img" style="left:88px;background:linear-gradient(160deg,#a6adb8,#5b6372)" role="img" aria-label="Smiling businessman in a meeting"></div>
<div class="photo svc-img" style="left:437px;background:linear-gradient(160deg,#dfe2e7,#9ea4ae)" role="img" aria-label="Professional holding a tablet"></div>
<div class="photo svc-img" style="left:789px;background:linear-gradient(160deg,#a9b0bb,#c89a6a)" role="img" aria-label="Man working on a laptop"></div>

<div class="abs svc-icon" style="left:199px">
  <svg width="40" height="40" viewBox="0 0 24 24" fill="none" stroke="#fff" stroke-width="1.5"><path d="M20 12a8 8 0 1 1-3-6.2M20 4v4h-4"/><path d="M12 8v4l3 2"/></svg>
</div>
<div class="abs svc-icon" style="left:550px">
  <svg width="40" height="40" viewBox="0 0 24 24" fill="none" stroke="#fff" stroke-width="1.5"><path d="M12 3l8 6-3 10H7L4 9z"/><circle cx="12" cy="12" r="2"/></svg>
</div>
<div class="abs svc-icon" style="left:901px">
  <svg width="40" height="40" viewBox="0 0 24 24" fill="none" stroke="#fff" stroke-width="1.5"><path d="M4 20h16M7 20l3-8 4 2 3-8"/><circle cx="17" cy="6" r="2"/></svg>
</div>

<div class="abs svc-label" style="left:114px">Order Fulfillment</div>
<div class="abs svc-label" style="left:464px">Price Savings</div>
<div class="abs svc-label" style="left:815px">Timely Delivery</div>

<!-- call band -->
<div class="abs cta"></div>
<div class="abs cta-title">We're On <em>Call 24/7</em> to React Promptly to Your Supply<br>Ordering Needs, Don't Hesitate to Call</div>
<div class="abs contact-bar"><span>+ (001) 555-0193</span><span>[or]</span><span>orders@clearlinesupply.example</span></div>

<!-- why choose us -->
<div class="photo why-photo" style="background:linear-gradient(100deg,#ffffff 0%,#e7e3df 35%,#b9a896 70%,#8d7a66 100%)" role="img" aria-label="Confident professional woman with arms crossed"></div>
<div class="abs eyebrow center" style="top:2311px;left:-1px"><span>WHY CHOOSE US</span></div>
<h2 class="abs h2 center" style="top:2348px;left:-1px">Why Choose Us</h2>

<div class="abs why-card" style="left:97px;top:2472px">
  <div class="ic"><svg width="34" height="34" viewBox="0 0 24 24" fill="none" stroke="#1b2233" stroke-width="1.5"><path d="M4 15v-3a8 8 0 0 1 16 0v3"/><rect x="3" y="14" width="4" height="6" rx="1"/><rect x="17" y="14" width="4" height="6" rx="1"/></svg></div>
  <h3>Client Focus</h3><p>Everything we do revolves around our clients and their needs</p>
</div>
<div class="abs why-card active" style="left:354px;top:2472px">
  <div class="ic"><svg width="38" height="38" viewBox="0 0 24 24" fill="none" stroke="#0ea2d0" stroke-width="1.5"><circle cx="12" cy="12" r="7"/><circle cx="12" cy="12" r="3"/><path d="M12 2v5M12 17v5M2 12h5M17 12h5"/></svg></div>
  <h3>Innovative Solutions</h3><p>Everything we do revolves around our clients and their needs</p>
</div>
<div class="abs why-card" style="left:609px;top:2472px">
  <div class="ic"><svg width="34" height="34" viewBox="0 0 24 24" fill="none" stroke="#1b2233" stroke-width="1.5"><path d="M20 11a8 8 0 0 0-14-4.5M4 4v3h3M4 13a8 8 0 0 0 14 4.5M20 20v-3h-3"/></svg></div>
  <h3>Cost-Effective</h3><p>Everything we do revolves around our clients and their needs</p>
</div>
<div class="abs why-card" style="left:97px;top:2756px">
  <div class="ic"><svg width="32" height="32" viewBox="0 0 24 24" fill="none" stroke="#1b2233" stroke-width="1.5"><circle cx="12" cy="8" r="4"/><path d="M4 21c0-4 4-6 8-6s8 2 8 6z"/></svg></div>
  <h3>Quality Assurance</h3><p>Everything we do revolves around our clients and their needs</p>
</div>
<div class="abs why-card" style="left:354px;top:2756px">
  <div class="ic"><svg width="32" height="32" viewBox="0 0 24 24" fill="none" stroke="#1b2233" stroke-width="1.5"><circle cx="11" cy="11" r="8"/><path d="M3 11h16M11 3c3 3 3 13 0 16M11 3c-3 3-3 13 0 16"/><circle cx="18" cy="18" r="3" fill="#f0f2f5"/></svg></div>
  <h3>Global Reach</h3><p>Everything we do revolves around our clients and their needs</p>
</div>
<div class="abs why-card" style="left:609px;top:2756px">
  <div class="ic"><svg width="34" height="34" viewBox="0 0 24 24" fill="none" stroke="#1b2233" stroke-width="1.5"><circle cx="12" cy="7" r="3"/><circle cx="5" cy="10" r="2"/><circle cx="19" cy="10" r="2"/><path d="M7 20c0-3 2-6 5-6s5 3 5 6zM2 18c0-2 1-4 3-4M22 18c0-2-1-4-3-4"/></svg></div>
  <h3>Cost-Effective</h3><p>Everything we do revolves around our clients and their needs</p>
</div>

<!-- testimonials -->
<div class="abs test-band"></div>
<div class="abs" style="left:0;top:3162px;width:1200px;text-align:center;font-size:12px;color:#fff"><span style="border-bottom:1px solid var(--teal);padding-bottom:3px">TESTIMONIALS</span></div>
<h2 class="abs h2 center" style="top:3197px;color:#fff">Reviews from Clients</h2>

<div class="abs t-card" style="left:112px">
  <div class="stars">★★★★★</div>
  <p>Lorem ipsum dolor sit amet, co nsectetur adipiscing elit, sed do eiusmod tempor incididunt ut labore et dolore</p>
  <hr>
  <div class="who"><div class="av" role="img" aria-label="Client portrait"></div><div><div class="nm">Mara Lindqvist</div><div class="rl">Human Resource</div></div></div>
</div>
<div class="abs t-card" style="left:461px">
  <div class="stars">★★★★★</div>
  <p>Lorem ipsum dolor sit amet, co nsectetur adipiscing elit, sed do eiusmod tempor incididunt ut labore et dolore</p>
  <hr>
  <div class="who"><div class="av" role="img" aria-label="Client portrait"></div><div><div class="nm">Mara Lindqvist</div><div class="rl">Human Resource</div></div></div>
</div>
<div class="abs t-card" style="left:807px">
  <div class="stars">★★★★★</div>
  <p>Lorem ipsum dolor sit amet, co nsectetur adipiscing elit, sed do eiusmod tempor incididunt ut labore et dolore</p>
  <hr>
  <div class="who"><div class="av" role="img" aria-label="Client portrait"></div><div><div class="nm">Mara Lindqvist</div><div class="rl">Human Resource</div></div></div>
</div>
<div class="abs quote" style="left:86px">“</div>
<div class="abs quote" style="left:435px">“</div>
<div class="abs quote" style="left:781px">“</div>

<!-- contact -->
<div class="abs eyebrow center" style="top:3718px"><span>CONTACT US</span></div>
<h2 class="abs h2 center" style="top:3752px">Get in touch with us</h2>

<div class="abs footer"></div>
<svg class="abs" style="left:0;top:4120px" width="1200" height="180" viewBox="0 0 1200 180">
  <path d="M0 60 C 200 150, 1000 150, 1200 60 L1200 0 L0 0 Z" fill="#fff"/>
  <path d="M1060 85 C 1130 110, 1175 150, 1200 200 L1200 120 C 1170 95, 1120 80, 1060 85 Z" fill="#0ea2d0"/>
</svg>

<div class="contact-card">
  <div class="photo contact-photo" style="background:linear-gradient(150deg,#dfe7f0,#7d97b5 60%,#2e4a72)" role="img" aria-label="Technicians inspecting a circuit board at a workstation"></div>
  <div class="abs form-brand"><span class="mark"></span>Clearline</div>
  <div class="abs form-title">Please fill out the form</div>
  <div class="abs field" style="left:512px;top:171px;width:360px;height:42px">Name</div>
  <div class="abs field" style="left:512px;top:224px;width:173px;height:41px">Phone</div>
  <div class="abs field" style="left:699px;top:224px;width:173px;height:41px">Email</div>
  <div class="abs field" style="left:512px;top:277px;width:360px;height:68px">Message</div>
  <div class="abs send">Send</div>
</div>

<!-- footer -->
<div class="abs footer-brand"><span class="mark"></span>Clearline Supply</div>
<div class="abs fnav">
  <span style="left:352px">HOME</span>
  <span style="left:445px">SERVICES</span>
  <span style="left:551px">ABOUT US</span>
  <span style="left:670px">TESTIMONIALS</span>
  <span style="left:820px">BLOG</span>
</div>
<div class="abs fline"></div>

<div class="abs finfo" style="left:172px">
  <div class="ring"><svg width="28" height="28" viewBox="0 0 24 24" fill="none" stroke="#fff" stroke-width="1.3"><circle cx="12" cy="12" r="9"/><path d="M3 12h18M12 3c3 3 3 15 0 18M12 3c-3 3-3 15 0 18"/></svg></div>
  <div>88 Harbor Lane, Suite 4<br>Lakeview, ST 10452</div>
</div>
<div class="abs fdiv" style="left:430px"></div>
<div class="abs finfo" style="left:505px">
  <div class="ring"><svg width="22" height="28" viewBox="0 0 16 24" fill="none" stroke="#fff" stroke-width="1.3"><rect x="3" y="2" width="10" height="20" rx="2"/><path d="M7 19h2"/></svg></div>
  <div><b>PHONE</b><br>(512) 555 0162</div>
</div>
<div class="abs fdiv" style="left:750px"></div>
<div class="abs finfo" style="left:828px">
  <div class="ring"><svg width="28" height="24" viewBox="0 0 24 20" fill="none" stroke="#fff" stroke-width="1.3"><rect x="2" y="3" width="20" height="14"/><path d="M2 3l10 8 10-8"/></svg></div>
  <div><b>EMAIL</b><br>hello@clearlinesupply.example</div>
</div>

<div class="abs bottom">
  <span class="copy">CLEARLINE SUPPLY</span>
  <span class="social" style="left:935px"></span>
  <span class="social" style="left:967px"></span>
  <span class="social" style="left:999px"></span>
  <span class="social" style="left:1031px"></span>
</div>

</body>
</html>
```